The Neighbors Together Project

For submission to Civic Drive 2024
Need both Color and Black and White Versions
TITLE The Neighbours Together Project
Slogan; "Neighbor's Together, same hopes...same Dreams, just a shades difference" -LM Brenner copyrights
Logo in Color and Logo in Black and White
Back of flyer will be The River of Quiet Lights poem -LM Brenner
VOTE BLUE 2024 Header or Footer

I just want to thank you all for your participation in The Neighbours Together Project. In the next few days I will be reducing the choices down to 10. Id like for all of you to know Ive enjoyed seeing so many options and views on the Flyer. Mainly, I wanted to say to those who don't make the cut that I appreciate the work you've done.

LM Doverly

```html
<!DOCTYPE html>
<html lang="en">
<head>
<meta charset="utf-8">
<title>The Neighbours Together Project – Flyer</title>
<link rel="stylesheet" href="https://fonts.googleapis.com/css2?family=Exo+2:wght@700;800&family=Source+Sans+3:wght@600;700&display=swap">
<style>
  :root {
    --stage: #d6d6d6;
    --paper: #ffffff;
    --flag-red: #b8292f;
    --flag-blue: #2b318f;
    --navy: #232a63;
    --ink: #111111;
    --white: #ffffff;
  }
  * { box-sizing: border-box; margin: 0; padding: 0; }
  html, body { width: 699px; height: 1200px; overflow: hidden; }
  body {
    background: var(--stage);
    position: relative;
    font-family: "Source Sans 3", "Myriad Pro", sans-serif;
  }
  .flyer-page {
    position: absolute;
    left: 157px;
    width: 386px;
    height: 545px;
    background: var(--paper);
    box-shadow: 3px 4px 8px rgba(0,0,0,.25);
    overflow: hidden;
  }
  .flyer-front { top: 39px; }
  .flyer-back { top: 620px; }

  /* front */
  .map-field {
    position: absolute;
    left: 0; right: 0; top: 60px; bottom: 0;
    background:
      linear-gradient(180deg, rgba(255,255,255,1) 0%, rgba(255,255,255,0) 42%),
      linear-gradient(100deg, var(--flag-blue) 0%, var(--flag-blue) 14%, var(--flag-red) 26%, var(--flag-red) 100%);
  }
  .brand-mark {
    position: absolute;
    top: 118px; left: 0; right: 0;
    display: flex; align-items: center; justify-content: center; gap: 8px;
    color: var(--navy);
    font-weight: 700;
    font-size: 15px;
  }
  .brand-dot {
    width: 12px; height: 12px; border-radius: 50%;
    background: var(--flag-red);
  }
  .front-title {
    position: absolute;
    top: 340px; left: 0; right: 0;
    text-align: center;
    font-family: "Exo 2", sans-serif;
    font-weight: 800;
    font-size: 34px;
    line-height: 36px;
    color: var(--white);
  }
  .front-slogan {
    position: absolute;
    top: 424px; left: 0; right: 0;
    text-align: center;
    font-weight: 700;
    font-size: 12.5px;
    line-height: 17px;
    color: var(--white);
  }

  /* back */
  .poem-panel {
    position: absolute;
    left: 0; top: 0; right: 0;
    height: 347px;
    background: var(--flag-blue);
    color: var(--white);
    text-align: center;
  }
  .poem-title {
    padding-top: 32px;
    font-family: "Exo 2", sans-serif;
    font-weight: 700;
    font-size: 25px;
    line-height: 30px;
  }
  .poem-author {
    margin-top: 2px;
    font-weight: 700;
    font-size: 13px;
  }
  .poem-body { margin-top: 14px; }
  .poem-verse {
    font-weight: 600;
    font-size: 10.2px;
    line-height: 13px;
    margin-bottom: 13px;
  }
  .vote-call {
    position: absolute;
    top: 314px; left: 0; right: 0;
    font-weight: 700;
    font-size: 13px;
  }
  .back-mark {
    position: absolute;
    top: 410px; left: 0; right: 0;
    display: flex; align-items: center; justify-content: center; gap: 7px;
    color: var(--ink);
    font-weight: 700;
    font-size: 13px;
  }
  .back-mark .brand-dot { background: var(--ink); width: 10px; height: 10px; }
  .site-url {
    position: absolute;
    top: 503px; left: 0; right: 0;
    text-align: center;
    font-weight: 700;
    font-size: 12.5px;
    color: var(--ink);
  }
</style>
</head>
<body>
  <section class="flyer-page flyer-front">
    <div class="map-field" role="img" aria-label="Silhouette map of the United States in blue and red"></div>
    <div class="brand-mark"><span class="brand-dot"></span>Neighbor's Together Project</div>
    <h1 class="front-title">The Neighbours<br>Together Project</h1>
    <p class="front-slogan">Neighbor's Together, shared hopes...<br>shared dreams, one street at a time</p>
  </section>

  <section class="flyer-page flyer-back">
    <div class="poem-panel">
      <h2 class="poem-title">River of Quiet Lights</h2>
      <p class="poem-author">By LM Brenner</p>
      <div class="poem-body">
        <p class="poem-verse">Beneath the evening bridges where the slow blue waters bend,<br>a hundred porch lamps glimmer like the greetings of a friend.</p>
        <p class="poem-verse">We are a town of many windows...amber, silver, gold and white,<br>each one a little lantern set to guide us through the night.</p>
        <p class="poem-verse">We came by road and river, from the mountains and the<br>plains. Bringing stories, bringing recipes...and learning names.</p>
        <p class="poem-verse">Free to plant, Free to gather, Free to speak or Free to<br>rest...sharing, building side by side, we give this place our best.</p>
        <p class="poem-verse">So let us keep the lamps lit, pass the light from hand to hand.<br>For together we grow stronger, on this river, in this land.</p>
      </div>
      <p class="vote-call">VOTE BLUE 2024</p>
    </div>
    <div class="back-mark"><span class="brand-dot"></span>Neighbors Together</div>
    <p class="site-url">www.neighborstogetherproject.org</p>
  </section>
</body>
</html>
```